Bright and beautiful business card for a coach

I'm a personal and business coach based in Perth, Australia. I need a business card that whilst subtle and elegant, will stand out and appeal on a table full of cards.

My business name is Fern Coaching and the business card must represent the warmth and brightness implied in the name, without being gimmicky. It must have a warmth and appeal and be easy to read.

I prefer clean, minimalist designs.

It must align with the feel of my website and socials: https://www.ferncoachingplex.com.au/
https://www.instagram.com/ferncoachingplexau/
https://www.facebook.com/ferncoachingplexau
Updates

Deadline appearing 2 days away and still haven't completed brief - seems mighty short

Hi Designers Thank you so much for taking the time to submit designs. I wonder if I could have explained myself a little better. Most of the designs that have been submitted look rather formal and many have quite corporate looking embellishments on them (to my eye). I would like softer, warmer, more organic. I’m open to people playing about and being more abstract, using softer embellishments (e.g the line drawing flowers and grasses I’ve used in my socials) incorporating other colours from my palette or like the social icons in my email signature (in PDF), perhaps playing with size/oversize, playing with the bleed. Please don’t be constrained by what I’ve already done, it merely needs to compliment. I’m sorry if I’m not using the right words or have led you astray. I’m no designer, but I’ve done my website, socials, email signature etc all myself (my logo was a design contest) and I was really hoping for my business card to be something more creative than I could have made with a template. Reminder: No black cards/sides please. Thank you 😊

Target Market(s)

Individuals, most likely but not all female. Creative thinkers. Likely professionals.

Industry/Entity Type

Business & Personal Coach

Contact Information for Business Card

(Fern Coaching Logo) Name: Marla Pendry; Title: Business & Personal Coach; Phone number: +61 (0)498 315807; Email: marla@ferncoachingplex.com.au; Website: https://ferncoachingplex.com.au; Social icons for Facebook, Instagram & LinkedIn: @ferncoachingplexAU. Optional strapline: "A thinking partner to help you cut through the noise"

Font styles to use
Sans Serif

Colors
00AB8E
00BBA5
67D7C9
C6EFE9
E9F9F6
59FF00
82FF00
B8FF75
E3FFCB
F4FFEA
FFC000
F8CF3A
FAE287
FDF2CF
FEFAEE

Requirements
Must have
• Must align with feel of my website and socials. Must have a pop of #FFC000 (possibly whole of one side, or at least a block). Bright or white background. Easy to read.
Nice to have
• Possibly incorporate the sunshine/grass picture I have used in website and socials - will upload.
Should not have
• Must not be black or dark. Not impersonal or corporate looking.

```html
<!DOCTYPE html>
<html lang="en">
<head>
<meta charset="utf-8">
<title>Fern Coaching – Business Card</title>
<link href="https://fonts.googleapis.com/css2?family=Poppins:ital,wght@0,400;0,500;1,400&display=swap" rel="stylesheet">
<style>
  :root {
    --backdrop: #ece9e4;
    --card: #ffffff;
    --mint: #c6e6dc;
    --sun: #ffc000;
    --clay: #c2782c;
    --olive: #cbc93c;
    --ink: #4d5b5e;
    --sun-text: #f7b500;
    --white: #ffffff;
  }
  * { margin: 0; padding: 0; box-sizing: border-box; }
  html, body { width: 900px; height: 1200px; overflow: hidden; }
  body {
    background: var(--backdrop);
    font-family: "Poppins", sans-serif;
    position: relative;
  }
  .card {
    position: absolute;
    left: 82px;
    width: 736px;
    height: 430px;
    background: var(--card);
    overflow: hidden;
    box-shadow: 0 8px 18px rgba(0,0,0,0.18);
  }
  .card--front { top: 140px; }
  .card--back { top: 630px; }
  .card__art { position: absolute; inset: 0; width: 736px; height: 430px; }

  .wordmark {
    position: absolute;
    font-family: "Poppins", sans-serif;
    font-weight: 500;
    white-space: nowrap;
  }

  /* front */
  .wordmark--front { left: 52px; top: 352px; font-size: 24px; color: var(--white); letter-spacing: 1px; }
  .contact { position: absolute; left: 403px; top: 124px; color: var(--ink); }
  .contact__name { font-size: 25px; font-weight: 500; letter-spacing: 1.5px; line-height: 1.2; text-transform: uppercase; }
  .contact__title { font-size: 16px; font-weight: 500; color: var(--sun-text); letter-spacing: 0.8px; text-transform: uppercase; margin-top: 2px; }
  .contact__lines { list-style: none; margin-top: 24px; font-size: 16px; line-height: 28px; }
  .social-band {
    position: absolute; left: 380px; right: 0; bottom: 0; height: 86px;
    background: var(--clay);
  }
  .social { position: absolute; left: 403px; top: 370px; display: flex; align-items: center; gap: 10px; color: var(--white); font-size: 16px; }
  .social__dot { width: 12px; height: 12px; border-radius: 50%; background: var(--white); }
  .sun-strip { position: absolute; top: 0; right: 0; width: 14px; height: 344px; background: var(--sun); }

  /* back */
  .wordmark--back { left: 0; right: 0; top: 196px; text-align: center; font-size: 44px; color: var(--sun-text); letter-spacing: 2px; }
  .strapline-band {
    position: absolute; top: 0; right: 0; width: 250px; height: 130px;
    background: var(--clay);
  }
  .strapline {
    position: absolute; right: 36px; top: 40px;
    text-align: right; color: var(--white); font-style: italic; font-size: 16px; line-height: 25px;
    white-space: nowrap;
  }
  .footer-band {
    position: absolute; left: 0; right: 0; bottom: 0; height: 76px;
    background: var(--olive);
  }
  .back-url { position: absolute; left: 38px; top: 376px; color: var(--white); font-size: 17px; }
  .sun-bar { position: absolute; right: 0; bottom: 76px; width: 250px; height: 10px; background: var(--sun); }
</style>
</head>
<body>

<section class="card card--front">
  <svg class="card__art" viewBox="0 0 736 430" xmlns="http://www.w3.org/2000/svg">
    <defs>
      <linearGradient id="meadow" x1="0" y1="0" x2="0.3" y2="1">
        <stop offset="0" stop-color="#fbf3d6"/>
        <stop offset="0.3" stop-color="#b9c85a"/>
        <stop offset="0.7" stop-color="#6c9a2c"/>
        <stop offset="1" stop-color="#3f6a1c"/>
      </linearGradient>
    </defs>
    <path class="photo-area" role="img" aria-label="Photo: sunlit green grass with a bright sun flare in the top left"
          d="M0 0 L300 0 C350 60 372 150 360 240 C350 320 320 390 290 430 L0 430 Z" fill="url(#meadow)"/>
  </svg>
  <div class="sun-strip"></div>
  <div class="social-band"></div>
  <div class="wordmark wordmark--front">Fern Coaching</div>
  <div class="contact">
    <h1 class="contact__name">Marla Pendry</h1>
    <p class="contact__title">Business &amp; Personal Coach</p>
    <ul class="contact__lines">
      <li>+61 (0)498 315807</li>
      <li>marla@ferncoachingplex.com.au</li>
      <li>ferncoachingplex.com.au</li>
    </ul>
  </div>
  <div class="social"><span class="social__dot"></span><span>@ferncoachingplexAU</span></div>
</section>

<section class="card card--back">
  <svg class="card__art" viewBox="0 0 736 430" xmlns="http://www.w3.org/2000/svg" role="img" aria-label="Soft decorative colour wash in mint, cream and warm yellow">
    <defs>
      <linearGradient id="wash" x1="0" y1="0" x2="1" y2="1">
        <stop offset="0" stop-color="#eef7f3"/>
        <stop offset="0.5" stop-color="#ffffff"/>
        <stop offset="1" stop-color="#fdf2cf"/>
      </linearGradient>
    </defs>
    <rect width="736" height="430" fill="url(#wash)"/>
  </svg>
  <div class="strapline-band"></div>
  <p class="strapline">A thinking partner to<br>help you cut through<br>the noise</p>
  <div class="wordmark wordmark--back">Fern Coaching</div>
  <div class="sun-bar"></div>
  <div class="footer-band"></div>
  <p class="back-url">ferncoachingplex.com.au</p>
</section>

</body>
</html>
```